BRISK SWEEP

Need a professional looking business card that can fit : Name, Title, Cell, and office phone numbers. On the flip side we would like a list of our services : Highway accident management and towing, Crime scene clean up, Illegal drug lab clean up, Drug disposal, and Hazardous materials clean up.

```html
<!DOCTYPE html>
<html lang="en">
<head>
<meta charset="utf-8">
<title>Brisk Sweep – Business Card</title>
<link rel="stylesheet" href="https://fonts.googleapis.com/css2?family=Merriweather:wght@400;700&family=Open+Sans:wght@400;600&display=swap">
<style>
  :root {
    --navy: #14294a;
    --navy-deep: #0f2240;
    --gold: #e1b52f;
    --white: #ffffff;
    --backdrop: #ece7df;
    --faint: rgba(255,255,255,0.08);
  }
  html, body {
    margin: 0;
    width: 1200px;
    height: 1023px;
    overflow: hidden;
    background: var(--backdrop);
  }
  .canvas {
    position: relative;
    width: 1200px;
    height: 1023px;
  }
  .card {
    position: absolute;
    top: 150px;
    width: 440px;
    height: 720px;
  }
  .card--front { left: 130px; }
  .card--back { left: 630px; }
  .card-shape {
    position: absolute;
    inset: 0;
  }
  .front-name {
    position: absolute;
    top: 190px;
    left: 0;
    width: 440px;
    text-align: center;
    font-family: "Merriweather", Georgia, serif;
    font-weight: 700;
    font-size: 40px;
    letter-spacing: 2px;
    color: var(--gold);
  }
  .identity {
    position: absolute;
    left: 70px;
    top: 500px;
    font-family: "Open Sans", Arial, sans-serif;
    color: var(--white);
  }
  .person {
    display: flex;
    align-items: baseline;
    gap: 12px;
    margin-bottom: 14px;
  }
  .person-name {
    font-family: "Merriweather", Georgia, serif;
    font-weight: 700;
    font-size: 30px;
    color: var(--gold);
  }
  .person-divider {
    width: 1px;
    height: 30px;
    background: var(--white);
    align-self: center;
  }
  .person-title {
    font-weight: 600;
    font-size: 24px;
  }
  .contact-list {
    list-style: none;
    margin: 0;
    padding: 0;
  }
  .contact-item {
    display: flex;
    align-items: center;
    gap: 14px;
    font-size: 24px;
    line-height: 36px;
  }
  .contact-icon { width: 18px; height: 18px; flex: none; }
  .back-mark {
    position: absolute;
    top: 150px;
    left: 0;
    width: 440px;
    text-align: center;
    font-family: "Merriweather", Georgia, serif;
    font-weight: 700;
    font-size: 40px;
    letter-spacing: 2px;
    color: var(--faint);
  }
  .services {
    position: absolute;
    left: 50px;
    top: 330px;
    width: 360px;
    font-family: "Merriweather", Georgia, serif;
    color: var(--white);
  }
  .services-heading {
    margin: 0 0 20px;
    font-size: 20px;
    font-weight: 700;
    color: var(--gold);
  }
  .service-list {
    list-style: none;
    margin: 0;
    padding: 0 0 0 20px;
  }
  .service-item {
    position: relative;
    padding-left: 28px;
    font-size: 17px;
    line-height: 24px;
    margin-bottom: 10px;
  }
  .service-item::before {
    content: "★";
    position: absolute;
    left: 0;
    top: 0;
    color: var(--gold);
    font-size: 16px;
  }
</style>
</head>
<body>
<main class="canvas">

  <section class="card card--front" aria-label="Business card front">
    <svg class="card-shape" width="440" height="720" viewBox="0 0 440 720" aria-hidden="true">
      <rect x="0" y="220" width="440" height="500" fill="var(--navy)"/>
      <circle cx="220" cy="220" r="220" fill="var(--white)"/>
      <circle cx="220" cy="220" r="212" fill="var(--navy)"/>
      <circle cx="220" cy="220" r="204" fill="none" stroke="var(--gold)" stroke-width="3"/>
      <circle cx="220" cy="220" r="150" fill="none" stroke="var(--gold)" stroke-width="2"/>
    </svg>
    <div class="front-name">BRISK SWEEP</div>

    <div class="identity">
      <div class="person">
        <span class="person-name">Your Name</span>
        <span class="person-divider"></span>
        <span class="person-title">CEO</span>
      </div>
      <ul class="contact-list">
        <li class="contact-item">
          <svg class="contact-icon" viewBox="0 0 18 18" aria-hidden="true"><rect x="4" y="1" width="10" height="16" rx="2" fill="none" stroke="var(--gold)" stroke-width="2"/></svg>
          12345 678910
        </li>
        <li class="contact-item">
          <svg class="contact-icon" viewBox="0 0 18 18" aria-hidden="true"><path d="M4 1l3 4-2 2c1 2 3 4 5 5l2-2 4 3-2 3C8 16 2 10 1 4z" fill="var(--gold)"/></svg>
          12345 678910
        </li>
        <li class="contact-item">
          <svg class="contact-icon" viewBox="0 0 18 18" aria-hidden="true"><rect x="1" y="4" width="16" height="11" fill="var(--gold)"/><path d="M1 4l8 6 8-6" fill="none" stroke="var(--navy)" stroke-width="1.5"/></svg>
          hello@brisksweep.com
        </li>
      </ul>
    </div>
  </section>

  <section class="card card--back" aria-label="Business card back">
    <svg class="card-shape" width="440" height="720" viewBox="0 0 440 720" aria-hidden="true">
      <path d="M0 220 A220 220 0 0 1 440 220 L440 720 L0 720 Z" fill="var(--navy)"/>
    </svg>
    <div class="back-mark">BRISK SWEEP</div>

    <div class="services">
      <h2 class="services-heading">Our services :</h2>
      <ul class="service-list">
        <li class="service-item">Highway accident management and towing,</li>
        <li class="service-item">Crime scene clean up,</li>
        <li class="service-item">Illegal drug lab clean up,</li>
        <li class="service-item">Drug disposal, and</li>
        <li class="service-item">Hazardous materials clean up</li>
      </ul>
    </div>
  </section>

</main>
</body>
</html>
```